GREEK DELICATESSEN FRONT AND SIDE SIGNAGE

This Greek shop will include both a retail store and a small commercial kitchen for cooking demonstrations, small catering events etc. with each of these two functions having their own logos which are included in this project. These two logos are included both as pdf and psd format so you can slightly adjust the colors if needed to match the background which we would like to be a shade (or shades) of blue.
The shop has two sides as per the attached pictures where the front larger signage of 14.35m X 1.23m will include the wording: GREEK FOOD WINE AND MORE followed by the TINY HARBOUR logo and after that we want to add the sentence AUTHENTIC HOME COOKING followed by the logo MARLA'S GREEK KITCHEN. Somewhere on the signage we must include our website which is www.savourbrindle.co.nz and our phone number which is 0800 PLUMTO.
The second side being being much smaller at 6.37m X 1.23m must only include the wording GREEK FOOD WINE AND MORE followed by the TINY HARBOUR logo and all above contact details.

Target Market(s)

RETAIL CUSTOMERS AND FOOD LOVERS

Industry/Entity Type

Retail

Colors
33a6d7
3176b5
0492cd
0255a3
85cae6

Requirements
Nice to have
• SMALL GREEK FLAG
Should not have
• GREEK RUINS, SANTORINI PHOTOS

```html
<!DOCTYPE html>
<html lang="en">
<head>
<meta charset="utf-8">
<title>Tiny Harbour – Front and Side Signage</title>
<link rel="stylesheet" href="https://fonts.googleapis.com/css2?family=Montserrat:wght@500;600;700&display=swap">
<style>
  :root {
    --stage: #7a7a7a;
    --white: #ffffff;
    --panel-white: #f7f7f7;
    --olive: #636b32;
    --olive-text: #5c6530;
    --lime: #a7c02f;
    --green: #3db54a;
    --blue: #2079a8;
  }
  html, body {
    margin: 0;
    width: 1200px;
    height: 490px;
    overflow: hidden;
    background: var(--stage);
    font-family: "Montserrat", sans-serif;
  }
  .sign {
    position: absolute;
    left: 77px;
    width: 1051px;
  }
  .sign svg.backdrop {
    position: absolute;
    inset: 0;
    display: block;
  }
  .sign .txt {
    position: absolute;
    margin: 0;
    line-height: 1;
    white-space: nowrap;
  }
  .sign-side { top: 66px; height: 91px; }
  .sign-front { top: 208px; height: 202px; }

  .brand {
    display: flex;
    align-items: center;
    font-weight: 700;
    color: var(--olive-text);
  }
  .brand .dot {
    border-radius: 50%;
    background: var(--lime);
    flex: none;
  }

  /* side sign */
  .sign-side .brand { left: 24px; top: 38px; font-size: 14px; gap: 7px; }
  .sign-side .brand .dot { width: 14px; height: 14px; }
  .sign-side .headline { right: 597px; top: 25px; font-size: 40px; font-weight: 700; color: var(--olive-text); }
  .sign-side .subline { right: 597px; top: 65px; font-size: 22px; font-weight: 700; color: var(--lime); }
  .sign-side .hosting { left: 501px; top: 24px; font-size: 17px; font-weight: 700; color: var(--white); }
  .sign-side .kitchen { left: 560px; top: 44px; font-size: 13px; font-weight: 700; color: var(--white); line-height: 1.15; text-align: center; }
  .sign-side .cooking { left: 685px; top: 15px; font-size: 19.5px; font-weight: 700; color: var(--white); line-height: 1.1; text-align: center; }
  .sign-side .phone { left: 858px; top: 25px; font-size: 23px; font-weight: 700; color: var(--white); }
  .sign-side .web { left: 858px; top: 56px; font-size: 12.5px; font-weight: 500; color: var(--white); }

  /* front sign */
  .sign-front .brand { left: 48px; top: 84px; font-size: 34px; gap: 10px; }
  .sign-front .brand .dot { width: 30px; height: 30px; }
  .sign-front .headline { right: 52px; top: 30px; font-size: 74px; font-weight: 700; color: var(--white); }
  .sign-front .subline { right: 52px; top: 99px; font-size: 46px; font-weight: 700; color: var(--lime); }
  .sign-front .contact {
    position: absolute;
    right: 52px;
    top: 150px;
    height: 52px;
    display: flex;
    align-items: center;
    color: var(--white);
  }
  .sign-front .web { font-size: 19px; font-weight: 500; }
  .sign-front .divider { width: 1px; height: 26px; background: var(--white); margin: 0 20px; opacity: .8; }
  .sign-front .phone { font-size: 31px; font-weight: 700; }
</style>
</head>
<body>

<section class="sign sign-side" aria-label="Side signage">
  <svg class="backdrop" width="1051" height="91" viewBox="0 0 1051 91" aria-hidden="true">
    <rect width="1051" height="91" fill="var(--panel-white)"/>
    <polygon points="470,0 815,0 859,91 513,91" fill="var(--olive)"/>
    <polygon points="815,0 1051,0 1051,91 859,91" fill="var(--blue)"/>
    <polygon points="0,46 19,91 0,91" fill="var(--lime)"/>
    <polygon points="470,0 482,0 494,26 482,26" fill="var(--lime)"/>
    <polygon points="835,42 843,42 864,91 856,91" fill="var(--lime)"/>
    <polygon points="1035,0 1051,0 1051,28" fill="var(--lime)"/>
  </svg>
  <div class="txt brand"><span class="dot"></span>TINY HARBOUR</div>
  <p class="txt headline">GREEK FOOD</p>
  <p class="txt subline">WINE AND MORE</p>
  <p class="txt hosting">HOSTING</p>
  <p class="txt kitchen">MARLA'S<br>GREEK KITCHEN</p>
  <p class="txt cooking">AUTHENTIC<br>HOME<br>COOKING</p>
  <p class="txt phone">0800 PLUMTO</p>
  <p class="txt web">www.savourbrindle.co.nz</p>
</section>

<section class="sign sign-front" aria-label="Front signage">
  <svg class="backdrop" width="1051" height="202" viewBox="0 0 1051 202" aria-hidden="true">
    <rect width="1051" height="202" fill="var(--panel-white)"/>
    <polygon points="385,0 1051,0 1051,202 472,202" fill="var(--olive)"/>
    <polygon points="450,150 1051,150 1051,202 472,202" fill="var(--blue)"/>
    <polygon points="414,96 426,96 472,202 460,202" fill="var(--green)"/>
  </svg>
  <div class="txt brand"><span class="dot"></span>TINY HARBOUR</div>
  <p class="txt headline">GREEK FOOD</p>
  <p class="txt subline">WINE AND MORE</p>
  <div class="contact">
    <span class="web">www.savourbrindle.co.nz</span>
    <span class="divider"></span>
    <span class="phone">0800 PLUMTO</span>
  </div>
</section>

</body>
</html>
```